Reach Far Goals Training Web Design and Launch!

A recently new business in Personal Coaching (Fitness) looking to have a professional website built along with using Coinwell system for payments. Ability to set up memberships would be great. Current site is www.rfgtrain.fit . I used that site to quickly put something together so that I could get started. Also looking to do something similar to www.morlandgym.com with a shop as well as challenges and leaderboards that members and non members alike can participate in. Would like to have a "meet the coaches" page option along with what I currently have on the site.

Target Market(s)

Men and Women 24-60 years old. Weight loss clients

Industry/Entity Type

Fitness

Coding

Coded - Design and coding required

Number of Pages Required

5+ page

Font styles to use
Sans Serif

Colors
33a6d7
f78f20
0255a3
0592cd

Requirements
Must have
• Coinwell or Payment integration. Photo gallery. Reviews page. Calender link for events. Donation location for Step4AllKin
Nice to have
• Would like to have a page dedicated to challenges/leaderboards. A way for members and non members to input their results of a posted challenge. Like to have similar pages that my current site www.rfgtrain.fit has. Ways to sign up for a membership. Meet the coaches and athletes. Gallery designed to call out award winning performances (podium or series wins), Meet the coaches and athletes.

```html
<!DOCTYPE html>
<html lang="en">
<head>
<meta charset="utf-8">
<title>Reach Far Goals Training</title>
<link href="https://fonts.googleapis.com/css2?family=Rajdhani:wght@600;700&family=Montserrat:ital,wght@0,400;0,500;0,600;0,700;1,400&display=swap" rel="stylesheet">
<style>
:root{
  --blue:#4b82c9;
  --blue-dark:#3d6fb3;
  --orange:#f7901e;
  --navy:#222d3b;
  --navy-deep:#1c2530;
  --ink:#1b1b1b;
  --text:#555a61;
  --line:#e4e6ea;
  --paper:#ffffff;
  --mist:#f5f6f8;
}
*{box-sizing:border-box;margin:0;padding:0}
html,body{width:1200px;height:3785px;overflow:hidden}
body{font-family:"Montserrat",sans-serif;color:var(--text);background:var(--paper);position:relative}
.abs{position:absolute}
.heading{font-family:"Rajdhani",sans-serif;font-weight:700;color:var(--ink);letter-spacing:2px;text-transform:uppercase}
.eyebrow{font-family:"Montserrat",sans-serif;font-weight:600;font-size:8px;letter-spacing:1.6px;color:var(--orange);text-transform:uppercase}
.center{left:0;width:1200px;text-align:center}
section,.site-footer{position:absolute;left:0;width:1200px}

/* hero */
.hero{top:0;height:485px;background:linear-gradient(120deg,#3b3f47 0%,#23262c 45%,#4a4c50 70%,#1d1f23 100%);overflow:hidden}
.hero-shade{position:absolute;inset:0;background:radial-gradient(ellipse at 50% 40%,rgba(255,255,255,.08),rgba(0,0,0,.35))}
.brand{position:absolute;left:232px;top:10px;width:120px;text-align:center}
.brand-dot{width:54px;height:54px;border-radius:50%;background:var(--blue);margin:0 auto 6px}
.brand-name{font-family:"Rajdhani",sans-serif;font-weight:700;font-size:14px;line-height:15px;color:var(--blue);letter-spacing:.5px}
.nav{position:absolute;top:29px;left:0;width:1200px;height:12px}
.nav a{position:absolute;font-size:9px;font-weight:700;color:#fff;text-decoration:none;letter-spacing:.3px}
.nav a.active{color:var(--blue)}
.pill{position:absolute;top:18px;height:30px;font-size:8.5px;font-weight:700;line-height:30px;text-align:center}
.pill.join{left:842px;width:66px;background:#fff;color:var(--blue);border-radius:15px 0 0 15px;border:2px solid var(--blue);line-height:26px}
.pill.login{left:904px;width:63px;background:var(--blue);color:#fff;border-radius:0 15px 15px 0}
.hero-title{top:200px;font-size:56px;letter-spacing:3px;color:#fff}
.hero-title em{font-style:normal;color:var(--orange)}
.hero-sub{top:264px;font-size:26px;letter-spacing:1.5px;color:#fff}
.btn{display:block;background:var(--orange);color:#fff;font-size:10px;font-weight:600;letter-spacing:.6px;text-align:center;text-transform:uppercase}
.hero-btn{left:545px;top:316px;width:112px;height:34px;line-height:34px}

/* who we are */
.about{top:485px;height:568px;background:var(--paper)}
.about .eyebrow{left:234px;top:61px}
.about .title{left:234px;top:76px;font-size:29px}
.timeline{position:absolute;left:252px;top:132px;width:2px;height:380px;background:var(--blue)}
.marker{position:absolute;left:243px;width:20px;height:20px;border-radius:50%;background:var(--blue);border:3px solid #dce7f5;color:#fff;font-size:8px;font-weight:700;text-align:center;line-height:14px}
.point{position:absolute;left:281px;width:310px}
.point h3{font-family:"Rajdhani",sans-serif;font-weight:700;font-size:16px;letter-spacing:1.5px;color:var(--blue);text-transform:uppercase;margin-bottom:8px}
.point p{font-size:9.4px;line-height:15px;color:#444}
.photo{position:absolute}
.about-photo-a{left:621px;top:60px;width:302px;height:398px;background:linear-gradient(160deg,#8a6d55,#3d5f99 55%,#b0533f)}
.about-photo-b{left:751px;top:204px;width:216px;height:308px;background:linear-gradient(170deg,#4d5560,#2f5fae 60%,#2a2f38)}
.about-btn{left:621px;top:418px;width:128px;height:40px;line-height:40px}

/* gallery */
.gallery{top:1053px;height:533px;background:var(--navy)}
.gallery .eyebrow{top:57px}
.gallery .title{top:72px;font-size:29px;color:#fff}
.filters{position:absolute;top:122px;left:0;width:1200px;text-align:center;font-size:8px;font-weight:500;color:#fff;letter-spacing:.3px}
.filters span{margin:0 13px}
.filters .on{text-decoration:underline;text-underline-offset:4px}
.g1{left:234px;top:160px;width:239px;height:160px;background:linear-gradient(135deg,#7d8186,#2c2f34)}
.g2{left:234px;top:328px;width:239px;height:126px;background:linear-gradient(135deg,#6f6a64,#35383d)}
.g3{left:480px;top:160px;width:240px;height:294px;background:linear-gradient(160deg,#8f7c6c,#3c7fb6 55%,#5a5b5e)}
.g4{left:729px;top:160px;width:238px;height:125px;background:linear-gradient(135deg,#d8cfc4,#8fb04a 55%,#a47a4e)}
.g5{left:729px;top:294px;width:238px;height:160px;background:linear-gradient(135deg,#3a4453,#2f78b4 60%,#1f2732)}

/* schedule */
.schedule{top:1586px;height:560px;background:var(--paper)}
.schedule .eyebrow{top:62px}
.schedule .title{top:86px;font-size:29px}
.table{position:absolute;left:234px;top:137px;width:733px;display:grid;grid-template-columns:63px repeat(7,1fr);border-left:1px solid var(--line)}
.table div{height:62px;border-right:1px solid var(--line);border-bottom:1px solid var(--line);display:flex;align-items:center;justify-content:center;text-align:center;font-size:8px;line-height:16px;font-weight:500;color:var(--blue);text-transform:uppercase}
.table .head{height:54px;background:#f1f2f4;color:var(--ink);font-weight:600;font-size:8.5px;letter-spacing:.5px;border-right:1px solid #d9dce0}
.table .corner{background:var(--navy)}
.table .time{color:var(--ink);font-weight:700;font-size:9px}

/* reviews */
.reviews{top:2146px;height:263px;background:linear-gradient(var(--paper) 0 116px,var(--mist) 116px)}
.review-box{position:absolute;left:234px;top:0;width:733px;height:209px;background:var(--blue)}
.review-box .eyebrow{left:43px;top:56px}
.review-title{position:absolute;left:42px;top:68px;font-size:29px;line-height:30px;color:#fff;letter-spacing:2px}
.stars{position:absolute;left:295px;top:37px;font-size:12px;letter-spacing:1px;color:var(--orange)}
.stars .off{color:#fff}
.quote{position:absolute;left:295px;top:62px;width:440px;font-size:14.6px;line-height:19.5px;font-style:italic;color:#fff}
.reviewer{position:absolute;left:295px;top:162px;font-size:9px;color:#fff;letter-spacing:.3px}
.reviewer b{font-weight:700}
.dots{position:absolute;left:686px;top:180px;white-space:nowrap}
.dots i{display:inline-block;width:8px;height:8px;border-radius:50%;border:1.5px solid #fff;margin-left:3px}
.dots i.on{background:#fff}

/* blog */
.blog{top:2409px;height:394px;background:var(--mist)}
.blog .eyebrow{top:0}
.blog .title{top:18px;font-size:29px}
.post-main{left:234px;top:72px;width:357px;height:262px;background:linear-gradient(150deg,#9b6d4d,#3f62a0 50%,#6b3b2e)}
.post-main .meta{position:absolute;left:22px;top:193px;color:#fff}
.post-main h4{position:absolute;left:22px;top:212px;width:300px;font-size:12.5px;line-height:18px;font-weight:500;color:#fff}
.meta{font-size:8px;font-weight:500;color:var(--ink)}
.meta .ic{display:inline-block;width:8px;height:8px;border:1.5px solid var(--orange);border-radius:50%;vertical-align:-1px;margin-right:4px}
.meta .gap{margin-left:14px}
.thumb{left:610px;width:125px;height:78px}
.t1{top:72px;background:linear-gradient(135deg,#e9e4dc,#c98e5a)}
.t2{top:164px;background:linear-gradient(135deg,#b9bcc1,#3b3f45)}
.t3{top:256px;background:linear-gradient(135deg,#d7d9dc,#8f4a5a 60%,#c4c7cb)}
.post{position:absolute;left:751px;width:216px}
.post h4{font-size:12.5px;font-weight:500;color:var(--ink);margin:7px 0 6px}
.post p{font-size:8px;line-height:15px;color:#555}

/* partners */
.partners{top:2803px;height:279px;background:var(--paper)}
.partners .eyebrow{top:56px}
.partners .title{top:74px;font-size:29px}
.arrow{position:absolute;top:182px;width:26px;height:26px;border-radius:50%;border:1px solid #c9ccd1}
.badge{position:absolute;top:139px;height:87px;border-radius:4px}
.b1{left:234px;width:134px;background:linear-gradient(90deg,#f08a5d,#3fa9a0)}
.b2{left:402px;width:128px;background:linear-gradient(#d9d9d9 0 70%,#e0322f 70%)}
.b3{left:600px;width:158px;background:#efe8d6}
.b4{left:795px;width:172px;background:#2c7fc6}

/* donate */
.donate{top:3082px;height:301px;background:linear-gradient(120deg,#f5962e,#f08a1c 60%,#f6a03d)}
.donate .eyebrow{top:57px;color:#fff}
.donate .title{top:76px;font-size:29px;color:var(--ink)}
.donate-copy{position:absolute;top:120px;left:330px;width:540px;text-align:center;font-size:11px;line-height:19px;letter-spacing:1.3px;font-weight:500;color:#fff}
.donate-btn{left:546px;top:192px;width:108px;height:31px;line-height:31px;background:var(--blue)}
.cards{position:absolute;top:238px;left:554px;display:flex;gap:3px}
.cards i{display:block;width:16px;height:11px;border-radius:2px;background:#fff;opacity:.9}

/* newsletter */
.newsletter{top:3383px;height:234px;background:var(--navy)}
.newsletter .eyebrow{top:51px}
.newsletter .title{top:66px;font-size:29px;color:#fff}
.newsletter-copy{position:absolute;top:110px;left:0;width:1200px;text-align:center;font-size:9px;font-weight:600;color:#fff}
.field{position:absolute;top:148px;height:34px;border:1px solid #fff;border-radius:17px;color:#fff;font-size:8.5px;line-height:32px;padding-left:20px}
.f1{left:303px;width:223px}
.f2{left:539px;width:222px}
.signup{position:absolute;left:777px;top:148px;width:122px;height:34px;border-radius:17px;background:var(--blue);color:#fff;font-size:10px;font-weight:700;text-align:center;line-height:34px}

/* footer */
.site-footer{top:3617px;height:168px;background:var(--navy-deep)}
.site-footer .brand{left:232px;top:22px}
.social{position:absolute;top:64px;display:flex;gap:6px;left:877px}
.social i{display:block;width:25px;height:25px;border-radius:50%;border:1.5px solid #fff}
.copyright{position:absolute;left:640px;top:101px;width:327px;text-align:right;font-size:8px;color:#fff}
</style>
</head>
<body>

<section class="hero">
  <div class="hero-shade" role="img" aria-label="Coach spotting a woman lifting dumbbells on a bench in a gym"></div>
  <div class="brand"><div class="brand-dot"></div><div class="brand-name">REACH FAR GOALS TRAINING</div></div>
  <nav class="nav">
    <a class="active" style="left:417px">HOME</a>
    <a style="left:469px">SHOP</a>
    <a style="left:518px">BLOG</a>
    <a style="left:567px">REVIEWS</a>
    <a style="left:632px">GALLERY</a>
    <a style="left:695px">ATHLETE</a>
    <a style="left:759px">CONTACT US</a>
  </nav>
  <div class="pill join">JOIN US</div>
  <div class="pill login">&#9786; LOGIN</div>
  <h1 class="abs center heading hero-title"><em>COACHES</em> WHO CARE</h1>
  <p class="abs center heading hero-sub">LET'S WORK OUT TOGETHER!</p>
  <a class="abs btn hero-btn">CONTACT ME</a>
</section>

<section class="about">
  <p class="abs eyebrow">Know about us</p>
  <h2 class="abs heading title">WHO WE ARE</h2>
  <div class="timeline"></div>
  <div class="marker" style="top:144px">1</div>
  <div class="marker" style="top:257px">2</div>
  <div class="marker" style="top:370px">3</div>
  <div class="point" style="top:144px">
    <h3>Coaches who care</h3>
    <p>Our coaches take your fitness goals seriously. We understand that losing weight and gaining muscle can be challenging, and our goal is to help you overcome hurdles and reach your goals. We analyze your body type, BMI, and metabolism, to create your individualized fitness plan.</p>
  </div>
  <div class="point" style="top:258px">
    <h3>Knowledgeable training expertise</h3>
    <p>With years of success and experience, we are capable of analyzing your body and creating a fitness plan that will help you reach your goals. Most plans include healthy eating and exercise, to ensure the best results for our clients. Our coaches will work with you to keep you on track and motivated to reach your goals.</p>
  </div>
  <div class="point" style="top:371px">
    <h3>Your success is our goal</h3>
    <p>We understand that adapting new fitness habits is difficult and often times fails. Our goal is to change your view on fitness, so that it becomes apart of who you are and your lifestyle. We strongly believe that if you practice healthy habits, you will be able to obtain a healthy lifestyle. As a team we will have you feeling your best and maybe even finding yourself competing in a competition or in obstacle course racing.</p>
  </div>
  <div class="photo about-photo-a" role="img" aria-label="Boxing coach holding pads for a woman throwing a punch"></div>
  <a class="abs btn about-btn">CONTACT ME &#10230;</a>
  <div class="photo about-photo-b" role="img" aria-label="Smiling coach in a blue shirt holding a tablet in the gym"></div>
</section>

<section class="gallery">
  <p class="abs center eyebrow">Results</p>
  <h2 class="abs center heading title">GALLERY</h2>
  <div class="filters"><span class="on">ALL</span><span>ATHLETE</span><span>FITNESS</span><span>NUTRITION</span><span>WEIGHTLOSS</span></div>
  <div class="photo g1" role="img" aria-label="Man doing a one-arm push-up on a gym floor"></div>
  <div class="photo g2" role="img" aria-label="Trainer guiding a woman through a seated exercise"></div>
  <div class="photo g3" role="img" aria-label="Coach and client reviewing a plan on a tablet"></div>
  <div class="photo g4" role="img" aria-label="Salad bowl, green apple and measuring tape on a table"></div>
  <div class="photo g5" role="img" aria-label="Man doing push-ups on dumbbells"></div>
</section>

<section class="schedule">
  <p class="abs center eyebrow">Events timetable</p>
  <h2 class="abs center heading title">EVENTS SCHEDULE</h2>
  <div class="table">
    <div class="head corner"><svg width="18" height="18" viewBox="0 0 18 18" fill="none" stroke="#fff" stroke-width="1.5"><rect x="2" y="4" width="14" height="12"/><path d="M2 8h14M6 2v4M12 2v4M6 11h2M10 11h2M6 14h2M10 14h2"/></svg></div>
    <div class="head">MONDAY</div><div class="head">TUESDAY</div><div class="head">WEDNESDAY</div><div class="head">THURSDAY</div><div class="head">FRIDAY</div><div class="head">SATURDAY</div><div class="head">SUNDAY</div>

    <div class="time">6.00 AM</div>
    <div>Cole Barrett<br>Always Ready</div><div></div><div>Camp Nutrition<br>Program</div><div>Get a Grip<br>Training</div><div></div><div>Functional<br>Fitness Training</div><div></div>

    <div class="time">8.00 AM</div>
    <div>Camp Nutrition<br>Program</div><div></div><div>Cole Barrett<br>Always Ready</div><div></div><div>Functional<br>Fitness Training</div><div></div><div>Get a Grip<br>Training</div>

    <div class="time">10.00 AM</div>
    <div></div><div>Functional<br>Fitness Training</div><div></div><div>Camp Nutrition<br>Program</div><div>Get a Grip<br>Training</div><div></div><div>Cole Barrett<br>Always Ready</div>

    <div class="time">5.00 PM</div>
    <div>Get a Grip<br>Training</div><div></div><div></div><div>Camp Nutrition<br>Program</div><div>Cole Barrett<br>Always Ready</div><div></div><div>Functional<br>Fitness Training</div>

    <div class="time">7.00 PM</div>
    <div></div><div>Get a Grip<br>Training</div><div></div><div>Cole Barrett<br>Always Ready</div><div>Functional<br>Fitness Training</div><div></div><div>Camp Nutrition<br>Program</div>
  </div>
</section>

<section class="reviews">
  <div class="review-box">
    <p class="abs eyebrow">Reviews</p>
    <h2 class="heading review-title">WHAT OUR<br>CLIENTS<br>SAY ABOUT US</h2>
    <div class="stars">★★★★<span class="off">★</span></div>
    <p class="quote">Lorem ipsum dolor sit amet, consectetur adipiscing elit. Nulla viverra dignissim congue. Fusce eu turpis egestas, sagittis nunc aliquet, dapibus arcu. Suspendisse diam mauris, egestas et nisl eu, euismod imperdiet arci.</p>
    <p class="reviewer"><b>DANA REYES</b> - CUSTOMER</p>
    <div class="dots"><i class="on"></i><i></i><i></i></div>
  </div>
</section>

<section class="blog">
  <p class="abs center eyebrow">Latest blog</p>
  <h2 class="abs center heading title">OUR BLOG</h2>
  <div class="photo post-main" role="img" aria-label="Boxing coach holding pads for a female boxer">
    <p class="meta"><span class="ic"></span>08 Feb, 2020<span class="gap"></span><span class="ic"></span>23 Comments</p>
    <h4>Lorem ipsum dolor sit amet, consectetur adipiscing elit.</h4>
  </div>
  <div class="photo thumb t1" role="img" aria-label="Protein shakes and healthy food on a counter"></div>
  <div class="post" style="top:72px"><p class="meta"><span class="ic"></span>08 Feb, 2020<span class="gap"></span><span class="ic"></span>23 Comments</p><h4>Ut accumsan felis purus</h4><p>Lorem ipsum dolor sit amet, consectetur adipiscing elit. Aenean sit amet pretium nisi.</p></div>
  <div class="photo thumb t2" role="img" aria-label="Woman stretching in a bright studio"></div>
  <div class="post" style="top:164px"><p class="meta"><span class="ic"></span>08 Feb, 2020<span class="gap"></span><span class="ic"></span>23 Comments</p><h4>Nulla porttitor quam in justo</h4><p>Lorem ipsum dolor sit amet, consectetur adipiscing elit. Aenean sit amet pretium nisi.</p></div>
  <div class="photo thumb t3" role="img" aria-label="Group fitness class training together"></div>
  <div class="post" style="top:256px"><p class="meta"><span class="ic"></span>08 Feb, 2020<span class="gap"></span><span class="ic"></span>23 Comments</p><h4>Duis nec mollis tortor</h4><p>Lorem ipsum dolor sit amet, consectetur adipiscing elit. Aenean sit amet pretium nisi.</p></div>
</section>

<section class="partners">
  <p class="abs center eyebrow">Our partners</p>
  <h2 class="abs center heading title">PARTNERS AND AFFILIATES</h2>
  <div class="arrow" style="left:171px"><svg width="24" height="24" viewBox="0 0 24 24" fill="none" stroke="#9aa0a8" stroke-width="1.5"><path d="M14 7l-5 5 5 5"/></svg></div>
  <div class="badge b1" role="img" aria-label="Partner badge"></div>
  <div class="badge b2" role="img" aria-label="Partner badge"></div>
  <div class="badge b3" role="img" aria-label="Partner badge"></div>
  <div class="badge b4" role="img" aria-label="Partner badge"></div>
  <div class="arrow" style="left:1002px"><svg width="24" height="24" viewBox="0 0 24 24" fill="none" stroke="#9aa0a8" stroke-width="1.5"><path d="M10 7l5 5-5 5"/></svg></div>
</section>

<section class="donate" role="img" aria-label="Orange-tinted photo of a race finish line">
  <p class="abs center eyebrow">Donate now</p>
  <h2 class="abs center heading title">HELP OUR CAUSE</h2>
  <p class="donate-copy">In 2020 we are looking to support Step4AllKin an organization focused on helping people move and giving all athletes the opportunity to cross the finish line! Your generous donation will fund our mission.</p>
  <a class="abs btn donate-btn">DONATE NOW</a>
  <div class="cards"><i></i><i></i><i></i><i></i><i></i></div>
</section>

<section class="newsletter">
  <p class="abs center eyebrow">Subscribe</p>
  <h2 class="abs center heading title">NEWSLETTER</h2>
  <p class="newsletter-copy">Sign up to hear from us about specials, sales, and events. As well as health and wellness updates.</p>
  <div class="field f1">Name</div>
  <div class="field f2">Email Address</div>
  <div class="signup">SIGN UP</div>
</section>

<footer class="site-footer">
  <div class="brand"><div class="brand-dot"></div><div class="brand-name">REACH FAR GOALS TRAINING</div></div>
  <div class="social"><i></i><i></i><i></i></div>
  <p class="copyright">Copyright © 2020 Reach Far Goals Training - All Rights Reserved.</p>
</footer>

</body>
</html>
```